Stationary, cards, memo form for 45 year old Investment Company
Brennor Equity Holdings Stationary
Simple
Dan Kessworth
President & CEO
517 Orchard Ridge Ave
Seattle, WA 98107-3815
Dan@Brennorcap.com
www.Brennorcap.com
Please design:
business card
Memo form
template that can be used from computer
The grey "L" in the circle may be used as a watermark.
This is a very low-key, sophisticated, company that provides investment for wealthy people and companies. Should be simple and elegant. Please error on the side of being more simple and straightforward...understated
This is the logo to use. Note grey "L" in circle may be used as a watermark.

```html
<!DOCTYPE html>
<html lang="en">
<head>
<meta charset="utf-8">
<title>Brennor Equity Holdings — Business Card Options</title>
<link rel="stylesheet" href="https://fonts.googleapis.com/css2?family=Tinos:wght@400;700&display=swap">
<style>
  :root {
    --board: #8c8c8c;
    --card: #ffffff;
    --green: #1f6b57;
    --ink: #2b2b2b;
    --soft-ink: #444444;
    --rule: #b9b9b9;
    --watermark: #e3e3e3;
    --label: #ffffff;
  }
  * { box-sizing: border-box; margin: 0; padding: 0; }
  html, body { width: 1200px; height: 823px; overflow: hidden; }
  body {
    background: var(--board);
    font-family: "Tinos", "Times New Roman", serif;
    position: relative;
  }
  .option-label {
    position: absolute;
    width: 500px;
    text-align: center;
    color: var(--label);
    font-size: 24px;
  }
  .card {
    position: absolute;
    width: 500px;
    height: 293px;
    background: var(--card);
    box-shadow: 6px 8px 14px rgba(0,0,0,0.45);
  }
  .front-1 { left: 67px;  top: 96px; }
  .back-1  { left: 629px; top: 96px; }
  .front-2 { left: 67px;  top: 482px; }
  .back-2  { left: 629px; top: 482px; }

  .brand {
    position: absolute;
    left: 96px;
    display: flex;
    align-items: center;
    color: var(--ink);
    font-weight: 400;
  }
  .brand-dot {
    width: 68px; height: 68px;
    border-radius: 50%;
    background: var(--green);
    margin-right: 18px;
  }
  .brand-name { line-height: 1; }
  .brand-name .primary { display: block; font-size: 40px; letter-spacing: 1px; }
  .brand-name .secondary { display: block; font-size: 13px; letter-spacing: 2.5px; margin-top: 5px; }

  .person { position: absolute; left: 89px; }
  .person-name { color: var(--green); font-size: 23px; }
  .person-title { color: var(--ink); font-size: 16px; margin-top: 2px; }

  .contact-divider {
    position: absolute;
    left: 269px;
    width: 1px;
    height: 112px;
    background: var(--rule);
  }
  .contact {
    position: absolute;
    left: 281px;
    font-size: 12px;
    color: var(--soft-ink);
    line-height: 19px;
  }
  .contact-line { display: flex; align-items: center; }
  .contact-line svg { width: 10px; height: 10px; margin-right: 6px; fill: var(--green); }

  .website {
    position: absolute;
    left: 0; width: 100%;
    text-align: center;
    color: var(--green);
    font-size: 14px;
    letter-spacing: 3px;
  }
  .website-rule {
    position: absolute;
    left: 12px; right: 12px;
    height: 1px;
    background: var(--rule);
  }
  .watermark {
    position: absolute;
    width: 190px; height: 190px;
    border-radius: 50%;
    background: var(--watermark);
  }
</style>
</head>
<body>

  <div class="option-label" style="left:67px; top:28px;">Business Card (Front) - Option 1</div>
  <div class="option-label" style="left:629px; top:28px;">Business Card (Back) - Option 1</div>
  <div class="option-label" style="left:67px; top:437px;">Business Card (Front) - Option 2</div>
  <div class="option-label" style="left:629px; top:437px;">Business Card (Back) - Option 2</div>

  <section class="card front-1">
    <div class="brand" style="top:38px;">
      <span class="brand-dot"></span>
      <span class="brand-name"><span class="primary">BRENNOR</span><span class="secondary">EQUITY HOLDINGS</span></span>
    </div>
    <div class="person" style="top:178px;">
      <div class="person-name">Dan Kessworth</div>
      <div class="person-title">President &amp; CEO</div>
    </div>
    <div class="contact-divider" style="top:146px;"></div>
    <div class="contact" style="top:146px;">
      <div>517 Orchard Ridge Ave</div>
      <div>Seattle, WA 98107-3815</div>
      <div class="contact-line"><svg viewBox="0 0 10 10"><path d="M2 0h2l1 3-1.5 1a6 6 0 0 0 2.5 2.5L7 5l3 1v2a2 2 0 0 1-2 2A8 8 0 0 1 0 2a2 2 0 0 1 2-2z"/></svg>2065550142</div>
      <div class="contact-line"><svg viewBox="0 0 10 10"><rect x="2.5" y="0" width="5" height="10" rx="1"/></svg>2065550178</div>
      <div class="contact-line"><svg viewBox="0 0 10 10"><rect x="0" y="4" width="10" height="6"/><rect x="2" y="0" width="6" height="4"/></svg>2065550193</div>
      <div class="contact-line"><svg viewBox="0 0 10 10"><path d="M0 2h10v6H0z" fill="none" stroke="#1f6b57" stroke-width="1"/><path d="M0 2l5 3.5L10 2" fill="none" stroke="#1f6b57" stroke-width="1"/></svg>Dan@Brennorcap.com</div>
    </div>
    <div class="website" style="top:266px;">www.Brennorcap.com</div>
  </section>

  <section class="card back-1">
    <div class="watermark" style="left:130px; top:17px;"></div>
    <div class="website" style="top:262px;">www.Brennorcap.com</div>
  </section>

  <section class="card front-2">
    <div class="brand" style="top:28px;">
      <span class="brand-dot"></span>
      <span class="brand-name"><span class="primary">BRENNOR</span><span class="secondary">EQUITY HOLDINGS</span></span>
    </div>
    <div class="person" style="top:128px;">
      <div class="person-name">Dan Kessworth</div>
      <div class="person-title">President &amp; CEO</div>
    </div>
    <div class="contact-divider" style="top:98px;"></div>
    <div class="contact" style="top:98px;">
      <div>517 Orchard Ridge Ave</div>
      <div>Seattle, WA 98107-3815</div>
      <div class="contact-line"><svg viewBox="0 0 10 10"><path d="M2 0h2l1 3-1.5 1a6 6 0 0 0 2.5 2.5L7 5l3 1v2a2 2 0 0 1-2 2A8 8 0 0 1 0 2a2 2 0 0 1 2-2z"/></svg>2065550142</div>
      <div class="contact-line"><svg viewBox="0 0 10 10"><rect x="2.5" y="0" width="5" height="10" rx="1"/></svg>2065550178</div>
      <div class="contact-line"><svg viewBox="0 0 10 10"><rect x="0" y="4" width="10" height="6"/><rect x="2" y="0" width="6" height="4"/></svg>2065550193</div>
      <div class="contact-line"><svg viewBox="0 0 10 10"><path d="M0 2h10v6H0z" fill="none" stroke="#1f6b57" stroke-width="1"/><path d="M0 2l5 3.5L10 2" fill="none" stroke="#1f6b57" stroke-width="1"/></svg>Dan@Brennorcap.com</div>
    </div>
    <div class="website-rule" style="top:222px;"></div>
    <div class="website" style="top:230px;">www.Brennorcap.com</div>
    <div class="website-rule" style="top:256px;"></div>
  </section>

  <section class="card back-2">
    <div class="watermark" style="left:141px; top:40px;"></div>
    <div class="website" style="top:258px;">www.Brennorcap.com</div>
  </section>

</body>
</html>
```